INNOVATIVE DESIGN NEEDED FOR FINANCIAL COMPANY

INTERNATIONAL FIRM IN HONG KONG NEEDS A MODERN BUSINESS CARD DESIGN. ONE SIDE ENGLISH OTHER SIDE IN CHINESE. WE ARE OPEN TO CHANGING FONTS AND COLOR. SHOULD BE A CARD THAT IS PROFESSIONAL DEALING WITH HIGH NET WORTH CLIENTELE. BOTH SIDES OF THE CARD WILL BE THE SAME, HOWEVER, THE WORDING ON ONE SIDE WILL BE ENGLISH AND THE OTHER SIDE IN CHINESE (CAN ASSIST IN THE LETTERING - CAN PROVIDE ONCE CARD DESIGN IS ACCEPTED.

Target Market(s)

Hong Kong/CHINA

Contact Information for Business Card

ATTRACTIVE MODERN

```html
<!DOCTYPE html>
<html lang="en">
<head>
<meta charset="utf-8">
<title>Hangyuen Asset Management – Business Card</title>
<link rel="stylesheet" href="https://fonts.googleapis.com/css2?family=Arimo:ital,wght@0,400;0,700;1,700&family=Noto+Sans+TC:wght@900&display=swap">
<style>
  :root {
    --backdrop: #e4e5e7;
    --card: #ffffff;
    --brand-green: #00935f;
    --brand-green-light: #04a574;
    --ink: #2b2b2b;
    --ink-soft: #555555;
    --on-green: #ffffff;
  }
  * { box-sizing: border-box; margin: 0; padding: 0; }
  html, body {
    width: 1200px; height: 1000px; overflow: hidden;
    background: var(--backdrop);
  }
  .stage {
    width: 1200px; height: 1000px;
    display: flex; align-items: center; justify-content: center;
  }
  .business-card {
    position: relative;
    width: 720px; height: 410px;
    background: var(--card);
    overflow: hidden;
    box-shadow: 0 10px 30px rgba(0,0,0,.12);
  }
  .card-dome {
    position: absolute; inset: 0;
    width: 720px; height: 410px;
  }
  .brand {
    position: absolute; top: 36px; left: 40px;
    display: flex; align-items: center; gap: 18px;
  }
  .brand-dot {
    width: 62px; height: 62px; border-radius: 50%;
    background: var(--brand-green);
    flex: none;
  }
  .brand-name {
    font-family: "Noto Sans TC", "Arimo", sans-serif;
    font-weight: 900;
    line-height: 1.1;
  }
  .brand-name-zh { color: var(--ink); font-size: 34px; letter-spacing: 4px; display: block; }
  .brand-name-en { color: var(--ink-soft); font-size: 18px; letter-spacing: 1.5px; display: block; margin-top: 2px; }
  .contact {
    position: absolute; left: 120px; width: 440px; top: 168px;
    text-align: center;
    color: var(--on-green);
    font-family: "Arimo", sans-serif;
    line-height: 1.32;
  }
  .person-name { font-size: 19px; font-weight: 400; }
  .person-title { font-size: 19px; font-weight: 700; font-style: italic; }
  .divider {
    width: 74px; height: 2px; background: var(--on-green);
    margin: 8px auto 8px;
  }
  .contact-line { font-size: 18px; font-weight: 700; white-space: nowrap; }
  .sep {
    display: inline-block; width: 8px; height: 8px; border-radius: 50%;
    background: var(--ink); margin: 0 8px; vertical-align: middle;
  }
</style>
</head>
<body>
<main class="stage">
  <article class="business-card">
    <svg class="card-dome" viewBox="0 0 720 410" aria-hidden="true">
      <defs>
        <linearGradient id="domeFill" x1="0" y1="0" x2="1" y2="0">
          <stop offset="0" stop-color="#00935f"/>
          <stop offset="1" stop-color="#04a574"/>
        </linearGradient>
      </defs>
      <circle cx="340" cy="490" r="345" fill="url(#domeFill)"/>
    </svg>

    <header class="brand">
      <span class="brand-dot"></span>
      <h1 class="brand-name">
        <span class="brand-name-zh">恒遠資產管理有限公司</span>
        <span class="brand-name-en">Hangyuen Asset Management Ltd</span>
      </h1>
    </header>

    <section class="contact">
      <p class="person-name">Daniel Wong</p>
      <p class="person-title">Chief Financial Officer</p>
      <div class="divider"></div>
      <p class="contact-line">Address 10, Building Name,</p>
      <p class="contact-line">1st Floor, Office 2, City, Country</p>
      <p class="contact-line">T: +85221000001<span class="sep"></span>F: +85221000000</p>
      <p class="contact-line">E: info@hyam-hk.com<span class="sep"></span>W: www.hyam-hk.com</p>
    </section>
  </article>
</main>
</body>
</html>
```